Letterhead Design for Law Firm that Specializes in Property Damage Litigation

We are looking for a redesign of our letterhead. Our current letterhead lists all of our current staff members and we'd like to come up with a design that does NOT list all of the staff members so that it does not need to be updated with every newly hired employee. Must be in editable format.

We are a law firm that specializes in property damage, so we need something that is professional, yet modern. The final design should use our existing logo and should use a blue color scheme (alternate colors would be gray, black, and white).

Industry/Entity Type

Legal

Colors
0054AA
0677BA
7BADD7
CADEEF
E8F1F8

```html
<!DOCTYPE html>
<html lang="en">
<head>
<meta charset="UTF-8">
<title>Hartwell Crane Osler — Letterhead</title>
<link href="https://fonts.googleapis.com/css2?family=Cinzel:wght@500;600&family=Barlow:wght@500&family=Roboto+Condensed:wght@400&display=swap" rel="stylesheet">
<style>
  :root {
    --backdrop: #0054AA;
    --paper: #FFFFFF;
    --navy: #1F3864;
    --brand-blue: #0054AA;
    --rule: #CADEEF;
    --icon: #B9D3EC;
    --gray: #5E5E5E;
  }
  * { margin: 0; padding: 0; box-sizing: border-box; }
  html, body { width: 1200px; height: 1000px; overflow: hidden; }
  body { background: var(--backdrop); position: relative; }
  .letterhead {
    position: absolute;
    left: 291px;
    top: 100px;
    width: 618px;
    height: 800px;
    background: var(--paper);
  }
  .firm-mark {
    position: absolute;
    left: 29px;
    top: 40px;
    display: flex;
    align-items: center;
    gap: 10px;
  }
  .firm-mark-square {
    width: 14px;
    height: 14px;
    background: var(--navy);
  }
  .firm-name {
    font-family: "Cinzel", serif;
    font-weight: 600;
    font-size: 22px;
    line-height: 1;
    letter-spacing: 1px;
    color: var(--navy);
  }
  .tagline {
    position: absolute;
    left: 29px;
    top: 111px;
    font-family: "Barlow", sans-serif;
    font-weight: 500;
    font-size: 8px;
    line-height: 10px;
    letter-spacing: 1.8px;
    color: var(--gray);
  }
  .header-rule {
    position: absolute;
    left: 270px;
    right: 29px;
    top: 116px;
    height: 1px;
    background: var(--rule);
  }
  .website {
    position: absolute;
    right: 29px;
    top: 86px;
    font-family: "Cinzel", serif;
    font-weight: 500;
    font-size: 12.5px;
    line-height: 16px;
    letter-spacing: 1.6px;
    color: var(--brand-blue);
  }
  .footer-rule {
    position: absolute;
    left: 29px;
    right: 29px;
    top: 710px;
    height: 1px;
    background: var(--rule);
  }
  .office {
    position: absolute;
    top: 723px;
    font-family: "Roboto Condensed", sans-serif;
    font-size: 9px;
    letter-spacing: 0.4px;
    color: var(--gray);
  }
  .office--philadelphia { left: 29px; }
  .office--new-jersey { left: 352px; }
  .office-title {
    font-family: "Cinzel", serif;
    font-weight: 600;
    font-size: 9.5px;
    line-height: 12px;
    letter-spacing: 1.2px;
    color: var(--brand-blue);
    margin-bottom: 6px;
  }
  .office-line {
    display: flex;
    align-items: center;
    gap: 4px;
    height: 17px;
    white-space: nowrap;
  }
  .office-line svg { width: 10px; height: 11px; flex: none; fill: var(--icon); }
</style>
</head>
<body>
  <main class="letterhead">
    <div class="firm-mark">
      <span class="firm-mark-square"></span>
      <span class="firm-name">Hartwell Crane Osler</span>
    </div>
    <div class="tagline">PROPERTY LOSS &amp; DAMAGE COUNSEL</div>
    <div class="header-rule"></div>
    <div class="website">WWW.HCOLEGAL.COM</div>

    <div class="footer-rule"></div>

    <section class="office office--philadelphia">
      <h2 class="office-title">PHILADELPHIA OFFICE</h2>
      <p class="office-line">
        <svg viewBox="0 0 24 24" aria-hidden="true"><path d="M6.6 10.8a15.1 15.1 0 0 0 6.6 6.6l2.2-2.2a1 1 0 0 1 1-.25 11.4 11.4 0 0 0 3.6.57 1 1 0 0 1 1 1V20a1 1 0 0 1-1 1A17 17 0 0 1 3 4a1 1 0 0 1 1-1h3.5a1 1 0 0 1 1 1c0 1.25.2 2.45.57 3.57a1 1 0 0 1-.25 1z"/></svg>
        215.555.0142&nbsp;&nbsp;|&nbsp;&nbsp;Fax: 215.555.0187
      </p>
      <p class="office-line">
        <svg viewBox="0 0 24 24" aria-hidden="true"><path d="M12 2a7 7 0 0 0-7 7c0 5.25 7 13 7 13s7-7.75 7-13a7 7 0 0 0-7-7zm0 9.5A2.5 2.5 0 1 1 12 6.5a2.5 2.5 0 0 1 0 5z"/></svg>
        2210 Market Street Suite 840 Philadelphia, PA 19103
      </p>
    </section>

    <section class="office office--new-jersey">
      <h2 class="office-title">NEW JERSEY OFFICE</h2>
      <p class="office-line">
        <svg viewBox="0 0 24 24" aria-hidden="true"><path d="M6.6 10.8a15.1 15.1 0 0 0 6.6 6.6l2.2-2.2a1 1 0 0 1 1-.25 11.4 11.4 0 0 0 3.6.57 1 1 0 0 1 1 1V20a1 1 0 0 1-1 1A17 17 0 0 1 3 4a1 1 0 0 1 1-1h3.5a1 1 0 0 1 1 1c0 1.25.2 2.45.57 3.57a1 1 0 0 1-.25 1z"/></svg>
        856.555.0163&nbsp;&nbsp;|&nbsp;&nbsp;Fax: 215.555.0187
      </p>
      <p class="office-line">
        <svg viewBox="0 0 24 24" aria-hidden="true"><path d="M12 2a7 7 0 0 0-7 7c0 5.25 7 13 7 13s7-7.75 7-13a7 7 0 0 0-7-7zm0 9.5A2.5 2.5 0 1 1 12 6.5a2.5 2.5 0 0 1 0 5z"/></svg>
        415 Haddonfield Road Suite 310 Cherry Hill, NJ 08002
      </p>
    </section>
  </main>
</body>
</html>
```